Cover for Where the Quiet River Bends Beyond Our Morning

Cover for a book that describes everything that happens to a person, from pre-birth life plans through growing in compassion and wisdom to death and living in the afterlife. The information is revealed in messages from people living in the life after this life. The title is Lanterns Along the Hidden Stair of Every Soul: Gathered from Voices Dwelling in the Further Meadow. Author is T. Morven Ashdale. Book size is 6 by 9.

Target Market(s)

General

Font styles to use
Serif

```html
<!DOCTYPE html>
<html lang="en">
<head>
<meta charset="utf-8">
<title>Lanterns Along the Hidden Stair of Every Soul — Cover</title>
<link rel="stylesheet" href="https://fonts.googleapis.com/css2?family=Allura&family=Source+Code+Pro:wght@700&display=swap">
<style>
  :root {
    --paper: #ffffff;
    --sky-blue: #2aa6dc;
    --rule-blue: #6cc4e6;
    --rule-pale: #a9dcf0;
    --plum: #6a3a8f;
    --violet-glow: rgba(150, 110, 190, 0.55);
    --blue-glow: rgba(95, 140, 205, 0.6);
    --ice-glow: rgba(160, 205, 235, 0.45);
    --amber-glow: rgba(245, 180, 110, 0.55);
    --coral-glow: rgba(230, 110, 80, 0.6);
  }
  html, body {
    margin: 0;
    padding: 0;
    width: 805px;
    height: 1200px;
    overflow: hidden;
    background: var(--paper);
  }
  .cover {
    position: relative;
    width: 805px;
    height: 1200px;
    background: var(--paper);
    overflow: hidden;
  }
  .cover-art {
    position: absolute;
    left: 0;
    top: 0;
    width: 805px;
    height: 1010px;
    background:
      radial-gradient(circle at 235px 55px, rgba(150, 80, 170, 0.55) 0, rgba(150, 80, 170, 0) 40px),
      radial-gradient(circle at 505px 85px, var(--amber-glow) 0, rgba(245, 180, 110, 0) 45px),
      radial-gradient(circle at 605px 270px, var(--coral-glow) 0, rgba(230, 110, 80, 0) 50px),
      radial-gradient(circle at 220px 930px, var(--amber-glow) 0, rgba(245, 180, 110, 0) 45px),
      radial-gradient(ellipse 260px 360px at 470px 420px, var(--blue-glow) 0, rgba(95, 140, 205, 0) 100%),
      radial-gradient(ellipse 330px 520px at 250px 560px, var(--violet-glow) 0, rgba(150, 110, 190, 0) 100%),
      radial-gradient(ellipse 300px 420px at 620px 380px, var(--ice-glow) 0, rgba(160, 205, 235, 0) 100%);
  }
  .rule {
    position: absolute;
    left: 182px;
    width: 444px;
  }
  .rule-top { top: 690px; }
  .rule-bottom { top: 1005px; }
  .title-block {
    position: absolute;
    left: 0;
    top: 715px;
    width: 805px;
    text-align: center;
  }
  .title-lead {
    font-family: "Allura", cursive;
    font-size: 38px;
    line-height: 1;
    color: var(--sky-blue);
    margin: 0 0 0 -150px;
  }
  .title-main {
    font-family: "Allura", cursive;
    font-size: 66px;
    line-height: 1.05;
    color: var(--sky-blue);
    margin: 0 0 0 60px;
    font-weight: 400;
  }
  .title-tail {
    font-family: "Allura", cursive;
    font-size: 44px;
    line-height: 1.1;
    color: var(--plum);
    margin: 0 0 0 -40px;
  }
  .subtitle {
    position: absolute;
    left: 0;
    top: 928px;
    width: 805px;
    text-align: center;
    font-family: "Source Code Pro", monospace;
    font-weight: 700;
    font-size: 21px;
    line-height: 31px;
    color: var(--sky-blue);
    margin: 0;
  }
  .author {
    position: absolute;
    left: 0;
    top: 1036px;
    width: 805px;
    text-align: center;
    font-family: "Source Code Pro", monospace;
    font-weight: 700;
    font-size: 27px;
    color: var(--sky-blue);
    margin: 0;
  }
</style>
</head>
<body>
<main class="cover">
  <div class="cover-art" role="img" aria-label="Outline of an open reaching hand drawn in thin white strokes over a soft violet and blue glow with scattered blurred amber, coral and plum lights"></div>

  <svg class="rule rule-top" width="444" height="8" viewBox="0 0 444 8" aria-hidden="true">
    <rect x="0" y="0" width="444" height="3" fill="var(--rule-blue)"/>
    <rect x="0" y="6" width="444" height="1.2" fill="var(--rule-pale)"/>
  </svg>

  <header class="title-block">
    <p class="title-lead">Lanterns Along</p>
    <h1 class="title-main">the Hidden Stair</h1>
    <p class="title-tail">of Every Soul</p>
  </header>

  <p class="subtitle">Gathered from Voices<br>Dwelling in the Further Meadow</p>

  <svg class="rule rule-bottom" width="444" height="8" viewBox="0 0 444 8" aria-hidden="true">
    <rect x="0" y="0" width="444" height="1.2" fill="var(--rule-pale)"/>
    <rect x="0" y="4" width="444" height="3" fill="var(--rule-blue)"/>
  </svg>

  <p class="author">By T. Morven Ashdale</p>
</main>
</body>
</html>
```